Flyer Designer for a Widow and Door Company - loooking for fresh design

We are looking for a flyer designed to advertise our business - we supply and install windows and doors - we are looking for a fresh looking flyer to distribute to drum up business - more information can be found at our website www.brightpanehouse.co.uk - We want a different approach than we currently have - making it vibrant and fresh - you can see the services on the website but its more the graphical design that we are looking for rather than content as the content from the website can be used for each service etc.

Target Market(s)

the general public

Colors

Designer to choose colors to be used in the design.

Requirements
Must have
• vibrant design and images

```html
<!DOCTYPE html>
<html lang="en">
<head>
<meta charset="utf-8">
<title>Bright Pane House – Flyer</title>
<link rel="stylesheet" href="https://fonts.googleapis.com/css2?family=Anton&family=Roboto:wght@400;500;700&display=swap">
<style>
  :root{
    --brand-blue:#4a72b5;
    --brand-blue-dark:#34589a;
    --paper:#ffffff;
    --ink:#222222;
    --page-bg:#e9e6e1;
  }
  *{margin:0;padding:0;box-sizing:border-box}
  html,body{width:1041px;height:1200px;overflow:hidden;background:var(--page-bg)}
  body{font-family:"Roboto",sans-serif;position:relative}
  .flyer{position:absolute;left:70px;top:20px;width:900px;height:1160px;background:var(--paper);overflow:hidden;box-shadow:0 4px 18px rgba(0,0,0,.12)}
  .flyer-shapes{position:absolute;inset:0}
  .brand{position:absolute;left:660px;top:86px;display:flex;align-items:center;gap:10px;color:var(--brand-blue);font-weight:700;font-size:27px;letter-spacing:.5px}
  .brand-mark{width:30px;height:30px;background:var(--brand-blue)}
  .welcome{position:absolute;left:15px;top:421px;width:244px;height:244px;display:flex;align-items:center;justify-content:center;text-align:center;font-family:"Anton",sans-serif;font-size:36px;line-height:46px;color:var(--ink);text-transform:uppercase}
  .section{position:absolute;left:20px;color:#fff}
  .section h2{font-weight:500;font-size:32px;line-height:1.2;display:inline-block;padding-bottom:4px;border-bottom:4px solid #fff;margin-bottom:12px}
  .section p{font-size:20px;line-height:26.5px;white-space:nowrap}
  .section--windows{top:712px}
  .section--windows h2{text-transform:uppercase}
  .section--doors{top:894px}
  .contact{position:absolute;left:547px;top:1052px;color:var(--ink);font-size:18px;line-height:25px}
  .contact b{color:var(--brand-blue);font-weight:500}
  .social{display:flex;align-items:center;gap:12px;margin-top:14px;margin-left:18px}
  .follow-pill{background:var(--brand-blue);color:#fff;font-weight:700;font-size:15px;padding:2px 16px;border-radius:14px;border:2px solid var(--brand-blue-dark);text-transform:uppercase}
  .social-dot{width:22px;height:22px;border-radius:50%;background:var(--brand-blue)}
</style>
</head>
<body>
<main class="flyer">
  <svg class="flyer-shapes" viewBox="0 0 900 1160" width="900" height="1160">
    <defs>
      <linearGradient id="windowsPhoto" x1="0" y1="0" x2="1" y2="1">
        <stop offset="0" stop-color="#eef0f2"/>
        <stop offset=".5" stop-color="#9aa59a"/>
        <stop offset="1" stop-color="#3e4a3f"/>
      </linearGradient>
      <linearGradient id="doorPhoto" x1="0" y1="0" x2="0" y2="1">
        <stop offset="0" stop-color="#5b6270"/>
        <stop offset=".55" stop-color="#2f3850"/>
        <stop offset="1" stop-color="#a9a39a"/>
      </linearGradient>
    </defs>
    <rect x="0" y="0" width="900" height="580" fill="url(#windowsPhoto)" role="img" aria-label="Photo of open white casement windows with garden reflections"/>
    <path d="M628 0 H900 V245 C800 238 690 262 650 190 C630 140 628 70 628 0 Z" fill="var(--paper)"/>
    <path d="M0 1160 V556 C170 558 420 560 560 470 C680 392 700 300 790 256 C840 236 880 234 900 234 V1160 Z" fill="var(--brand-blue)"/>
    <path d="M440 1160 C500 1100 530 1008 640 994 C760 980 860 990 900 960 V1160 Z" fill="var(--paper)"/>
    <circle cx="137" cy="543" r="136" fill="var(--paper)" stroke="var(--brand-blue)" stroke-width="8"/>
    <rect x="618" y="381" width="256" height="517" rx="14" fill="url(#doorPhoto)" stroke="#fff" stroke-width="4" role="img" aria-label="Photo of a navy composite front door with glazed panel and potted plants"/>
  </svg>

  <div class="brand"><span class="brand-mark"></span>Bright Pane House</div>

  <div class="welcome">Welcome<br>to Bright<br>Pane<br>House</div>

  <section class="section section--windows">
    <h2>Our Windows</h2>
    <p>Our windows are individually designed to suit your home.<br>Bespoke to your individual requirements. Our windows offer<br>an exceptional level of energy efficiency with market leading<br>locking systems.</p>
  </section>

  <section class="section section--doors">
    <h2>Our Doors</h2>
    <p>A new door from Bright Pane House can<br>transform the look of your home, offer increased<br>thermal efficiency and dramatically improve<br>security for your peace of mind. With literally<br>hundreds of different designs, colours and<br>finishes to choose from, contact us<br>today for a free, no obligation quotation.</p>
  </section>

  <div class="contact">
    <div><b>TEL</b> - 01632960418</div>
    <div><b>EMAIL</b> - sales@brightpanehouse.co.uk</div>
    <div class="social">
      <span class="follow-pill">Follow us</span>
      <span class="social-dot"></span>
      <span class="social-dot"></span>
      <span class="social-dot"></span>
    </div>
  </div>
</main>
</body>
</html>
```